Bluerock Custom Water Tank

I primarily market the water tanks so want a business care that reflects that. I have attached the water tank logo. You have been working on our water tank so maybe we can use that on the card et. I am leaving as one sided but can be double sided if that works. The information that needs to be on the cards is as follows: Dennis K. Marlow Phone numbers: Office 555-318-4720 Direct 555-260-9134 Mobile 555-482-1657 email address: dennis@fieldgearsupply.example Address P.O. Box 3827 Lakemont, GA 30519 Web Page: www.fieldgearsupply.example. A lot to fit on the card. Thanks

```html
<!DOCTYPE html>
<html lang="en">
<head>
<meta charset="utf-8">
<title>Bluerock Custom Water Tank – Business Card</title>
<link rel="stylesheet" href="https://fonts.googleapis.com/css2?family=Poppins:wght@400;600;700&display=swap">
<style>
  :root {
    --backdrop: #5cc6e6;
    --card: #f6f6f4;
    --ink: #2b2b2b;
    --accent: #e3323b;
    --font: "Poppins", sans-serif;
  }
  html, body {
    margin: 0;
    padding: 0;
    width: 1200px;
    height: 900px;
    overflow: hidden;
    background: var(--backdrop);
    font-family: var(--font);
  }
  .card {
    position: absolute;
    left: 150px;
    top: 105px;
    width: 900px;
    height: 690px;
    background: var(--card);
    color: var(--ink);
  }
  .brand {
    position: absolute;
    left: 48px;
    top: 225px;
    width: 340px;
  }
  .brand-mark {
    width: 64px;
    height: 64px;
    background: var(--accent);
    margin-bottom: 22px;
  }
  .brand-name {
    margin: 0;
    font-weight: 700;
    font-size: 28px;
    line-height: 1.15;
    color: var(--ink);
    white-space: nowrap;
  }
  .divider {
    position: absolute;
    left: 414px;
    top: 125px;
    width: 3px;
    height: 470px;
    background: var(--accent);
  }
  .person {
    position: absolute;
    left: 440px;
    top: 140px;
    margin: 0;
  }
  .person-first {
    display: block;
    font-weight: 400;
    font-size: 56px;
    line-height: 1.05;
    color: var(--accent);
  }
  .person-last {
    display: block;
    font-weight: 700;
    font-size: 58px;
    line-height: 1.05;
    color: var(--ink);
  }
  .phones-label {
    position: absolute;
    left: 442px;
    top: 318px;
    margin: 0;
    font-size: 20px;
    font-weight: 400;
  }
  .phone {
    position: absolute;
    margin: 0;
    font-size: 17px;
    font-weight: 400;
    white-space: nowrap;
  }
  .phone-office { left: 442px; top: 372px; }
  .phone-mobile { left: 442px; top: 410px; }
  .phone-direct { left: 668px; top: 400px; }
  .web-contact {
    position: absolute;
    left: 442px;
    top: 478px;
    margin: 0;
    font-size: 21px;
    line-height: 1.75;
    white-space: nowrap;
  }
  .address {
    position: absolute;
    left: 62px;
    top: 612px;
    margin: 0;
    font-size: 16px;
    white-space: nowrap;
  }
</style>
</head>
<body>
  <article class="card">
    <div class="brand">
      <div class="brand-mark"></div>
      <p class="brand-name">Bluerock<br>Custom Water Tank</p>
    </div>

    <div class="divider"></div>

    <h1 class="person">
      <span class="person-first">Dennis</span>
      <span class="person-last">K. Marlow</span>
    </h1>

    <p class="phones-label">Phone numbers:</p>
    <p class="phone phone-office">Office 555-318-4720</p>
    <p class="phone phone-mobile">Mobile 555-482-1657</p>
    <p class="phone phone-direct">Direct 555-260-9134</p>

    <p class="web-contact">
      dennis@fieldgearsupply.example<br>
      www.fieldgearsupply.example
    </p>

    <p class="address">3827 Lakemont, GA 30519</p>
  </article>
</body>
</html>
```